Business Card Design and Logo Needed

I need Business Cards and a Logo for my website and public speaking business which can be found at: www.kelsa-thorn.example

I'm looking for creative and unique ideas. Some business cards I've found online that I like can be found at:
http://gigplatelo.example/general/18-smokin-hot-business-card-designs/

and at

http://www.vortaplume.example/2009/04/50-creative-business-cards-of-50-graphic-designers/

```html
<!DOCTYPE html>
<html lang="en">
<head>
<meta charset="utf-8">
<title>Kelsa Thorn – Business Card Front</title>
<link rel="stylesheet" href="https://fonts.googleapis.com/css2?family=Crimson+Text:ital,wght@0,400;0,700;1,400;1,700&family=Lato:wght@400&display=swap">
<style>
  :root {
    --page-bg: #ffffff;
    --wine: #8e1b1f;
    --ink: #2a2320;
    --gold: #a98b4c;
    --parchment-light: #f6f0e2;
    --parchment-mid: #eadcbc;
    --parchment-edge: #b48c4e;
    --parchment-burn: #6e4a24;
    --wood: #5d3f27;
    --label-red: #c0393b;
  }
  * { margin: 0; padding: 0; box-sizing: border-box; }
  html, body {
    width: 1200px; height: 900px; overflow: hidden;
    background: var(--page-bg);
  }
  .canvas { position: relative; width: 1200px; height: 900px; }

  .card {
    position: absolute; left: 63px; top: 153px;
    width: 1084px; height: 604px;
    background: var(--wood);
    box-shadow: 4px 6px 10px rgba(0,0,0,0.35);
    overflow: hidden;
  }
  .card__parchment {
    position: absolute; left: 24px; top: 0; right: 10px; bottom: 0;
    background:
      radial-gradient(ellipse 62% 62% at 50% 48%,
        var(--parchment-light) 0%, var(--parchment-light) 55%,
        var(--parchment-mid) 78%, var(--parchment-edge) 93%, var(--parchment-burn) 100%);
  }

  .card__content {
    position: absolute; inset: 0;
    font-family: "Crimson Text", Georgia, serif;
    text-align: center;
  }
  .brand-mark {
    position: absolute; left: 0; right: 0; top: 138px;
    font-weight: 700; font-size: 80px; line-height: 1;
    color: var(--wine);
  }
  .holder-name {
    position: absolute; left: 0; right: 0; top: 358px;
    font-weight: 700; font-style: italic; font-size: 56px; line-height: 1;
    color: var(--wine);
  }
  .holder-role {
    position: absolute; left: 0; right: 0; top: 412px;
    font-style: italic; font-size: 35px; line-height: 1;
    color: var(--wine);
  }
  .divider {
    position: absolute; left: 193px; top: 464px;
    width: 698px; height: 10px;
  }
  .contact {
    position: absolute; left: 0; right: 0;
    font-size: 30px; line-height: 1; color: var(--ink);
  }
  .contact--first { top: 489px; }
  .contact--second { top: 525px; }
  .contact__label { color: var(--wine); font-weight: 700; }

  .view-label {
    position: absolute; left: 0; width: 1172px; top: 782px;
    text-align: center;
    font-family: "Lato", Arial, sans-serif;
    font-size: 56px; color: var(--label-red);
  }
</style>
</head>
<body>
<div class="canvas">
  <div class="card">
    <div class="card__parchment" role="img" aria-label="Aged parchment texture with burnt, darkened edges over a wooden backing"></div>
    <div class="card__content">
      <div class="brand-mark">Kelsa Thorn</div>
      <div class="holder-name">Kelsa Thorn</div>
      <div class="holder-role">Speaker, Philanthropist, and Author</div>
      <svg class="divider" viewBox="0 0 698 10" aria-hidden="true">
        <line x1="5" y1="5" x2="693" y2="5" stroke="var(--gold)" stroke-width="2"/>
        <circle cx="5" cy="5" r="4" fill="var(--gold)"/>
        <circle cx="693" cy="5" r="4" fill="var(--gold)"/>
      </svg>
      <p class="contact contact--first">
        <span class="contact__label">mobile:</span> 0491 570 156
        <span class="contact__label">email:</span> kelsa@kelsa-thorn.example
      </p>
      <p class="contact contact--second">
        <span class="contact__label">website:</span> kelsa-thorn.example
      </p>
    </div>
  </div>
  <div class="view-label">front</div>
</div>
</body>
</html>
```